NZ First of it's kind solutions directory and marketplace for busy Mums needs a business card design

We need a business card design for our new nationwide business in NZ (long term plans to go global). We provide solutions to the everyday challenges that busy Mums face by connecting them with quality communities and suppliers of carefully selected, relevant products and services. We sell direct via our online marketplace. The final design should communicate our values of inclusivity, quality and smart solutions. Colours should incorporate our logo colour palette of #477077 and #6ba8b2. Our website is at https://www.brightnestly.com

Target Market(s)

busy Mums, Age 28 – 50, female, income over $100K, location main centres NZ primarily but NZ wide. Is likely juggling work or career with a young family. Probably had hobbies which have fallen by the wayside.
-Wants to succeed in her chosen career without compromising on family life
-to successfully juggle her career without feeling like she is compromising her children
- Is time poor, something always has to give and it’s generally her health (she’ll stay up late, get stressed)
- probably ex corporate or professional career. Has discretional income

Industry/Entity Type

Business

Contact Information for Business Card

Jodie Farnsworth, Founder, BrightNestly.com (Strapline Browse; Pick; Sorted), 48 Kowhai Terrace, Hillsborough, Auckland 1058, New Zealand. Mob: 021 437 518 Ph: +64 (0)9 584 7163

Font styles to use
Other font styles liked:
• Raleway, and/or Architects Daughter

Colors
00a990
33b8a4
86cfc6
cfeae6

Requirements
Must have
• the above details, streamline. the logo and colours associated with those logos
Should not have
• foil or metallic colours

```html
<!DOCTYPE html>
<html lang="en">
<head>
<meta charset="utf-8">
<title>BrightNestly — Business Card</title>
<link rel="stylesheet" href="https://fonts.googleapis.com/css2?family=Raleway:wght@300;400;700;800&family=Arimo:wght@400&display=swap">
<style>
  :root {
    --ink: #3d5a60;
    --brand-dark: #477077;
    --brand-light: #6ba8b2;
    --panel: #6a9c9a;
    --tab: #3f5e63;
    --paper: #ffffff;
    --shadow: #e6e6e2;
  }
  * { margin: 0; padding: 0; box-sizing: border-box; }
  html, body { width: 1006px; height: 1200px; overflow: hidden; background: var(--paper); }
  .sheet { position: relative; width: 1006px; height: 1200px; background: var(--paper); font-family: "Raleway", sans-serif; }
  .shapes { position: absolute; inset: 0; }
  .abs { position: absolute; white-space: nowrap; line-height: 1; }

  .brand-name { font-family: "Raleway", sans-serif; font-weight: 800; color: var(--ink); letter-spacing: -1px; }
  .front-brand { left: 232px; top: 227px; font-size: 92px; }
  .back-brand { left: 100px; top: 878px; font-size: 50px; }

  .front-url { left: 0; width: 1006px; text-align: center; top: 470px; font-family: "Arimo", sans-serif; font-size: 28px; color: var(--ink); }

  .person { right: 22px; top: 700px; font-size: 48px; color: #fff; font-weight: 300; }
  .person strong { font-weight: 800; }
  .role { left: 752px; width: 120px; text-align: center; top: 760px; font-size: 29px; font-weight: 400; color: #fff; }

  .contact { font-family: "Arimo", sans-serif; font-size: 25px; color: #fff; }
  .contact-web { left: 601px; top: 898px; }
  .contact-mobile { left: 577px; top: 977px; }
  .contact-phone { left: 544px; top: 1054px; }
  .contact-address { left: 514px; top: 1122px; line-height: 34px; }
  .contact-address span { display: block; padding-left: 7px; }
</style>
</head>
<body>
<div class="sheet">
  <svg class="shapes" width="1006" height="1200" viewBox="0 0 1006 1200" aria-hidden="true">
    <!-- front card -->
    <circle class="brand-dot" cx="145" cy="262" r="48" fill="var(--ink)"/>
    <circle cx="303" cy="486" r="9" fill="var(--ink)"/>
    <circle cx="702" cy="486" r="9" fill="var(--ink)"/>
    <rect class="band-light" x="0" y="511" width="1006" height="17" fill="var(--brand-light)"/>
    <rect class="band-dark" x="0" y="527" width="1006" height="48" fill="var(--brand-dark)"/>

    <!-- back card -->
    <polygon class="panel" points="604,625 1006,625 1006,1200 388,1200" fill="var(--panel)"/>
    <circle cx="53" cy="898" r="26" fill="var(--ink)"/>

    <g class="tabs" fill="var(--tab)">
      <polygon points="517,859 592,859 561,932 487,932"/>
      <polygon points="489,940 561,940 532,1014 458,1014"/>
      <polygon points="458,1021 530,1021 498,1094 425,1094"/>
      <polygon points="427,1104 499,1104 467,1176 395,1176"/>
    </g>

    <!-- envelope -->
    <g class="icon-mail" fill="#fff" stroke="var(--tab)" stroke-width="2">
      <rect x="515" y="881" width="50" height="32"/>
      <polyline points="515,881 540,901 565,881" fill="none"/>
    </g>
    <!-- phone handset -->
    <path class="icon-phone" fill="#fff" d="M495 958 l10 -4 l8 14 l-7 5 q4 10 14 16 l6 -6 l13 9 l-4 10 q-8 5 -20 -2 q-18 -12 -24 -30 q-3 -8 4 -12z"/>
    <!-- fax -->
    <g class="icon-fax" fill="#fff">
      <rect x="452" y="1045" width="9" height="34" rx="3"/>
      <rect x="463" y="1050" width="37" height="28" rx="3"/>
      <rect x="471" y="1040" width="22" height="12"/>
      <g fill="var(--tab)">
        <circle cx="474" cy="1062" r="2"/><circle cx="482" cy="1062" r="2"/><circle cx="490" cy="1062" r="2"/>
        <circle cx="474" cy="1070" r="2"/><circle cx="482" cy="1070" r="2"/><circle cx="490" cy="1070" r="2"/>
      </g>
    </g>
    <!-- pin -->
    <path class="icon-pin" fill="#fff" fill-rule="evenodd" d="M448 1122 a13 13 0 0 1 13 13 q0 9 -13 27 q-13 -18 -13 -27 a13 13 0 0 1 13 -13z M448 1129 a5 5 0 1 0 0.01 0z"/>
  </svg>

  <div class="abs brand-name front-brand">BrightNestly</div>
  <div class="abs front-url">www.brightnestly.com</div>

  <div class="abs brand-name back-brand">BrightNestly</div>

  <div class="abs person">Jodie <strong>Farnsworth</strong></div>
  <div class="abs role">Founder</div>

  <div class="abs contact contact-web">www.brightnestly.com</div>
  <div class="abs contact contact-mobile">021 437 518</div>
  <div class="abs contact contact-phone">+64 (0)9 584 7163</div>
  <div class="abs contact contact-address">48 Kowhai Terrace, Hillsborough,<span>Auckland 1058, New Zealand</span></div>
</div>
</body>
</html>
```